LPS AUDITION

I need a post card design (front only) with this on it:
Leap Pulse Stride (this is the main title to be in all caps)
Auditions
Date: Thursday June 30th
6:30-8:30 PM in person
Address: 4172 Kestrel BLVD, Oakland CA 94605
video submissions turn in by Sunday July 3rd, 2022 email:LeapPulseStride22@movenote.test
Teens and Adults welcomed

SO PLEASE COME UP WITH A DESIGN THATS COLORFUL AND INVITING THX!

```html
<!DOCTYPE html>
<html lang="en">
<head>
<meta charset="utf-8">
<title>Leap Pulse Stride Auditions Postcard</title>
<link href="https://fonts.googleapis.com/css2?family=Montserrat:wght@400;600;700;800;900&display=swap" rel="stylesheet">
<style>
  :root {
    --backdrop: #2a2922;
    --paper: #ffffff;
    --pill-green: #3a9638;
    --pill-green-dark: #23702a;
    --date-red: #c21f2b;
    --title-orange: #e08c2a;
    --title-magenta: #c41a8c;
    --title-white: #ffffff;
    --band-yellow: #fff21a;
    --band-lime: #9ccb2e;
    --band-green: #2e9b47;
    --band-deep: #1f8a4b;
    --ink: #2b2b22;
    --icon-red: #d42a2a;
  }
  * { margin: 0; padding: 0; box-sizing: border-box; }
  html, body {
    width: 1200px; height: 956px; overflow: hidden;
    background: var(--backdrop);
    font-family: "Montserrat", Arial, sans-serif;
  }
  .postcard {
    position: absolute; left: 50px; top: 89px;
    width: 1100px; height: 778px;
    background: var(--paper);
    overflow: hidden;
  }
  .color-band {
    position: absolute; left: 0; top: 406px; width: 100%; height: 372px;
    background: linear-gradient(65deg, var(--band-yellow) 0%, var(--band-lime) 35%, var(--band-green) 75%, var(--band-deep) 100%);
  }
  .dancers-photo {
    position: absolute; left: 470px; top: 0; width: 630px; height: 640px;
    background:
      radial-gradient(ellipse 48% 44% at 62% 48%, rgba(160,170,190,0.95) 0%, rgba(150,175,120,0.85) 45%, rgba(0,0,0,0) 72%),
      radial-gradient(ellipse 60% 55% at 55% 20%, rgba(247,236,40,0.9) 0%, rgba(247,236,40,0) 70%),
      radial-gradient(ellipse 55% 50% at 75% 85%, rgba(40,140,70,0.85) 0%, rgba(40,140,70,0) 70%);
  }
  .audition-tag {
    position: absolute; left: 56px; top: 37px;
    width: 152px; height: 31px; border-radius: 8px;
    background: linear-gradient(var(--pill-green), var(--pill-green-dark));
    color: #fff; font-weight: 700; font-size: 20px; line-height: 31px;
    text-align: center;
  }
  .session-info {
    position: absolute; left: 56px; top: 84px;
    color: var(--date-red); font-weight: 700; font-size: 25px; line-height: 32px;
  }
  .headline {
    position: absolute; left: 50px; top: 0; z-index: 2;
    font-weight: 900; text-transform: uppercase; line-height: 1;
  }
  .headline span { position: absolute; left: 0; white-space: nowrap; letter-spacing: -3px; }
  .headline .word-leap { top: 180px; font-size: 145px; color: var(--title-orange); }
  .headline .word-pulse { top: 282px; font-size: 145px; color: var(--title-magenta); }
  .headline .word-stride { top: 378px; font-size: 218px; color: var(--title-white); letter-spacing: -6px; }
  .venue {
    position: absolute; left: 54px; top: 620px; z-index: 3; color: var(--ink);
  }
  .venue-label { font-size: 22px; font-weight: 400; line-height: 30px; }
  .venue-address { font-size: 22px; font-weight: 700; line-height: 32px; }
  .submission {
    position: absolute; left: 53px; top: 704px; z-index: 3;
    display: flex; align-items: center; gap: 16px; color: var(--ink);
    font-size: 22px; line-height: 28px;
  }
  .submission strong { font-weight: 700; }
  .contact {
    position: absolute; left: 482px; top: 718px; z-index: 3;
    display: flex; align-items: center; gap: 18px;
    color: var(--ink); font-size: 25px; font-weight: 600;
  }
</style>
</head>
<body>
  <main class="postcard">
    <div class="color-band"></div>
    <div class="dancers-photo" role="img" aria-label="Photo of two hip-hop dancers leaping mid-air over a yellow and green halftone burst"></div>

    <div class="audition-tag">Auditions</div>
    <p class="session-info">Date: Thursday June 30th<br>6:30-8:30 PM in person</p>

    <h1 class="headline">
      <span class="word-leap">Leap</span>
      <span class="word-pulse">Pulse</span>
      <span class="word-stride">Stride</span>
    </h1>

    <div class="venue">
      <p class="venue-label">Address:</p>
      <p class="venue-address">4172 Kestrel BLVD, Oakland CA 94605</p>
    </div>

    <div class="submission">
      <svg width="34" height="34" viewBox="0 0 34 34" aria-hidden="true">
        <rect x="1" y="1" width="32" height="32" rx="3" fill="#2b2b22"/>
        <path d="M11 8 L26 17 L11 26 Z" fill="var(--icon-red)"/>
      </svg>
      <p>video submissions turn in<br>by <strong>Sunday July 3rd, 2022</strong></p>
    </div>

    <div class="contact">
      <svg width="36" height="26" viewBox="0 0 36 26" aria-hidden="true">
        <rect x="1.5" y="1.5" width="33" height="23" fill="none" stroke="#111" stroke-width="3"/>
        <path d="M2 2 L18 15 L34 2" fill="none" stroke="#111" stroke-width="3"/>
        <path d="M2 24 L13 12 M34 24 L23 12" stroke="#111" stroke-width="3"/>
      </svg>
      <span>LeapPulseStride22@movenote.test</span>
    </div>
  </main>
</body>
</html>
```